Tova Brisk Fitness Coaching Project

I am a personal trainer based in London. My services include one-on-one PT sessions, bootcamps.
I would like the design to be minimalistic. With light colours: white, pink, purple.
I specialise in weight loss, flexibility, mobility.

Tova Penrick
Personal Trainer
Email: tova.penrick@mailgrove.net
tel: 07500 918 243
Instagram: Tova Brisk

Target Market(s)

adults, mostly females (age 18-50).

Industry/Entity Type

Fitness

Contact Information for Business Card

Tova Penrick
Personal Trainer
tel: 07500 918 243
Instagram: Tova Brisk

Font styles to use
Serif

Colors
eea4c8
fbd4d5
fdf9cf
cfeae6
cee9f5

Requirements
Nice to have
• minimalistic style
• easy to read and remember

```html
<!DOCTYPE html>
<html lang="en">
<head>
<meta charset="utf-8">
<title>Tova Brisk Fitness Coaching – Business Card</title>
<link rel="stylesheet" href="https://fonts.googleapis.com/css2?family=Mulish:wght@400;800&display=swap">
<style>
  :root {
    --stage: #f3eeee;
    --card-pink: #fbe3e8;
    --card-pink-soft: #fdf0f3;
    --band-pink: #d9759f;
    --band-pink-light: #eea4c8;
    --logo-pink: #e08ab0;
    --edge-blue: #cee9f5;
    --edge-mint: #cfeae6;
    --photo-dark: #4a3528;
    --photo-warm: #c98a55;
    --photo-light: #f1d7b6;
    --white: #ffffff;
  }
  * { box-sizing: border-box; margin: 0; padding: 0; }
  html, body { width: 1200px; height: 900px; overflow: hidden; }
  body {
    background: var(--stage);
    font-family: "Mulish", "Century Gothic", sans-serif;
    position: relative;
  }
  .card {
    position: absolute;
    left: 250px;
    width: 700px;
    height: 400px;
    overflow: hidden;
    box-shadow: 0 6px 18px rgba(90, 60, 60, 0.18);
  }
  .card--front { top: 40px; background: linear-gradient(160deg, var(--card-pink-soft), var(--card-pink)); }
  .card--back  { top: 480px; }

  .card__shapes { position: absolute; inset: 0; width: 100%; height: 100%; }

  .brand {
    position: absolute;
    display: flex;
    align-items: center;
    gap: 14px;
    font-weight: 400;
    letter-spacing: 1px;
  }
  .brand__dot { width: 18px; height: 18px; border-radius: 50%; flex: none; }

  .card--front .brand { left: 200px; top: 70px; font-size: 46px; color: var(--logo-pink); }
  .card--front .brand__dot { background: var(--logo-pink); }

  .contact {
    position: absolute;
    left: 30px;
    top: 272px;
    list-style: none;
    color: var(--white);
    font-size: 16px;
    line-height: 27px;
  }
  .contact__item { display: flex; align-items: center; gap: 10px; }
  .contact__icon { width: 16px; height: 16px; flex: none; }
  .contact__dot { width: 13px; height: 13px; margin: 0 1.5px; border: 2px solid var(--white); border-radius: 50%; flex: none; }

  .identity {
    position: absolute;
    right: 30px;
    bottom: 34px;
    text-align: right;
    color: var(--white);
  }
  .identity__name { font-weight: 800; font-size: 26px; line-height: 1.1; }
  .identity__role { font-weight: 400; font-size: 20px; }

  .card__wash {
    position: absolute;
    inset: 0;
    background:
      linear-gradient(180deg, transparent 0%, transparent 22%, rgba(207,234,230,0.85) 35%, rgba(206,233,245,0.75) 50%, rgba(251,212,213,0.7) 62%, transparent 75%),
      linear-gradient(100deg, #fce4ea 0%, #f8d6de 45%, #fbe6ec 100%);
  }
  .card--back .brand {
    left: 50%;
    top: 50%;
    transform: translate(-50%, -50%);
    font-size: 54px;
    color: var(--white);
  }
  .card--back .brand__dot { background: var(--white); }
</style>
</head>
<body>

  <section class="card card--front" aria-label="Business card front">
    <svg class="card__shapes" viewBox="0 0 700 400" aria-hidden="true">
      <defs>
        <linearGradient id="photoTone" x1="0" y1="0" x2="1" y2="0.6">
          <stop offset="0" stop-color="var(--photo-dark)"/>
          <stop offset="0.5" stop-color="var(--photo-warm)"/>
          <stop offset="1" stop-color="var(--photo-light)"/>
        </linearGradient>
      </defs>
      <polygon class="band band--light" points="0,140 476,288 458,300 0,172" fill="var(--band-pink-light)" opacity="0.55"/>
      <polygon class="band band--main" points="0,172 458,300 330,400 0,400" fill="var(--band-pink)"/>
      <polygon class="edge edge--blue" points="700,94 700,118 336,400 306,400" fill="var(--edge-blue)"/>
      <polygon class="edge edge--mint" points="700,118 700,124 344,400 336,400" fill="var(--edge-mint)"/>
    </svg>
    <svg class="card__shapes" viewBox="0 0 700 400" role="img" aria-label="Portrait photograph of the trainer">
      <polygon points="700,124 700,400 344,400" fill="url(#photoTone)"/>
    </svg>

    <div class="brand">
      <span class="brand__name">Tova Penrick</span>
      <span class="brand__dot"></span>
    </div>

    <ul class="contact">
      <li class="contact__item">
        <svg class="contact__icon" viewBox="0 0 16 16" aria-hidden="true"><path d="M4 1.5 6.2 4 5 6c.9 2 2.5 3.7 4.7 4.8l2-1.3 2.6 2.3-1.6 2.5C7.4 14 2 8.5 1.6 3.2Z" fill="var(--white)"/></svg>
        <span>07500 918 243</span>
      </li>
      <li class="contact__item">
        <svg class="contact__icon" viewBox="0 0 16 16" aria-hidden="true"><rect x="1" y="3" width="14" height="10" rx="1" fill="var(--white)"/><path d="M1.5 3.5 8 9l6.5-5.5" stroke="var(--band-pink)" stroke-width="1.4" fill="none"/></svg>
        <span>tova.penrick@mailgrove.net</span>
      </li>
      <li class="contact__item">
        <span class="contact__dot"></span>
        <span>Tova Brisk</span>
      </li>
    </ul>

    <div class="identity">
      <p class="identity__name">Tova Penrick</p>
      <p class="identity__role">Personal Trainer</p>
    </div>
  </section>

  <section class="card card--back" aria-label="Business card back">
    <div class="card__wash" role="img" aria-label="Soft pink and blue watercolour wash"></div>
    <div class="brand">
      <span class="brand__name">Tova Penrick</span>
      <span class="brand__dot"></span>
    </div>
  </section>

</body>
</html>
```